1/2 Page add for BRMTL Conference

We are looking for a 1/2 page ad to support the annual BRMTL conference. I want to encourage the attendees to come to our both so we can explain how they can save money on food and supplies. here is a link to the conference. https://www.brmtl-example.org/conference/ here is our website www.pantrywisehub-example.com - the what we do can be captured in the ad. We will be at booth 505. Our goal is to get people to our booth #505 to explain the services that we provide –

Discounted food pricing
Free menu planning/design
Use of Registered Dietitian
Huge selection of discounted PPE and other necessary supplies to run any child care center

We have over 6000 members in 46 States and work with both small and large food distributors. We have been a sponsor of the association for the last 10 years.

Target Market(s)

Child care centers

Requirements
Must have
• Booth number -outline of what we do --- Stress we are a FREE service getting our members reduced pricing on food and supplies

```html
<!DOCTYPE html>
<html lang="en">
<head>
<meta charset="utf-8">
<title>PantryWise Hub – Booth 505</title>
<link href="https://fonts.googleapis.com/css2?family=Barlow:wght@300;400;500;600;700&display=swap" rel="stylesheet">
<style>
  :root{
    --navy:#2e3192;
    --ink:#29286b;
    --green:#00a54f;
    --blue-text:#1c75bc;
    --paper:#f1f1f2;
    --white:#ffffff;
    --grey-name:#6d6e71;
  }
  *{margin:0;padding:0;box-sizing:border-box}
  html,body{width:691px;height:1200px;overflow:hidden;background:var(--white)}
  body{font-family:"Barlow",Arial,sans-serif;color:var(--ink)}
  .ad{position:relative;width:691px;height:1200px;background:var(--paper);overflow:hidden}
  .header-art{position:absolute;left:0;top:0;width:691px;height:483px;display:block}
  .hero-photo{
    position:absolute;left:0;top:144px;width:691px;height:339px;
    background:radial-gradient(ellipse 55% 70% at 50% 45%, #5a63c4 0%, #3b44a8 45%, var(--navy) 100%);
    clip-path:polygon(0 62px,691px 0,691px 339px,0 339px);
  }
  .brand{position:absolute;left:150px;top:64px}
  .brand-name{font-weight:300;font-size:52px;color:var(--grey-name);letter-spacing:-0.5px;line-height:1;display:flex;align-items:center;gap:14px}
  .brand-mark{width:34px;height:34px;background:var(--green);display:inline-block}
  .brand-tagline{margin:8px 0 0 48px;font-size:16px;font-weight:600;color:var(--blue-text)}
  .booth{
    position:absolute;left:196px;top:444px;width:306px;height:81px;
    background:var(--green);border-radius:12px;color:var(--white);
    font-weight:700;font-size:54px;line-height:81px;text-align:center;letter-spacing:0.5px;
  }
  .event{position:absolute;left:0;top:533px;width:691px;text-align:center;font-weight:700;font-size:40px;line-height:48px}
  .event-year{color:var(--ink)}
  .event-name{color:var(--green)}
  .pitch{position:absolute;left:62px;top:642px;font-size:24.5px;line-height:32px;font-weight:500}
  .pitch .lead{color:var(--blue-text)}
  .pitch strong{color:var(--ink);font-weight:700}
  .pitch .rest{color:var(--green)}
  .services-title{position:absolute;left:62px;top:736px;font-size:23px;font-weight:700;color:var(--green);padding-bottom:7px;border-bottom:2px solid var(--green);width:305px}
  .services{position:absolute;left:30px;top:781px;list-style:none;font-size:24px;font-weight:500;line-height:38px;color:var(--ink)}
  .services li{position:relative;padding-left:32px}
  .services li::before{content:"";position:absolute;left:4px;top:12px;width:14px;height:14px;background:var(--green)}
  .facts{position:absolute;left:0;top:995px;width:691px;height:160px;background:var(--green);color:var(--white);padding:22px 0 0 42px;font-weight:700}
  .facts::before{content:"";position:absolute;left:20px;right:20px;top:0;height:10px;background:radial-gradient(ellipse 50% 100% at 50% 0,rgba(0,40,20,.55),transparent)}
  .facts-lead{font-size:22px;line-height:24px}
  .facts-big{font-size:41px;line-height:48px}
  .facts-small{font-size:16px;line-height:29px;font-weight:600}
  .site{position:absolute;left:0;top:1155px;width:691px;height:45px;background:var(--navy);color:var(--white);font-size:23px;line-height:45px;text-align:center;font-weight:500}
</style>
</head>
<body>
<main class="ad">
  <svg class="header-art" viewBox="0 0 691 483" aria-hidden="true">
    <rect width="691" height="483" fill="var(--navy)"/>
    <polygon points="0,83 691,20 691,144 0,206" fill="var(--paper)"/>
    <polygon points="197,34 691,19 691,61" fill="var(--green)"/>
  </svg>
  <div class="hero-photo" role="img" aria-label="Photo of a smiling young child raising both open hands against a blue backdrop"></div>

  <div class="brand">
    <div class="brand-name"><span class="brand-mark"></span>PantryWise Hub</div>
    <div class="brand-tagline">Smart Savings for Care</div>
  </div>

  <div class="booth">booth 505</div>

  <h1 class="event">
    <span class="event-year">2022 BRMTL</span><br>
    <span class="event-name">Annual Conference</span>
  </h1>

  <p class="pitch">
    <span class="lead">we are a <strong>FREE service</strong> getting our members</span><br>
    <span class="rest">reduced pricing on food and supplies</span>
  </p>

  <h2 class="services-title">Services that we provide</h2>
  <ul class="services">
    <li>Discounted food pricing</li>
    <li>Free menu planning/design</li>
    <li>Use of Registered Dietitian</li>
    <li>Huge selection of discounted PPE and other<br>necessary supplies to run any child care center</li>
  </ul>

  <section class="facts">
    <p class="facts-lead">We have over</p>
    <p class="facts-big">6000 members in 46 States</p>
    <p class="facts-small">and work with both small and large food distributors.<br>We have been a sponsor of the association for the last 10 years.</p>
  </section>

  <footer class="site">www.pantrywisehub-example.com</footer>
</main>
</body>
</html>
```